Wine Lable

We Are Marlowby Ridge Wines and we are designing a new bottle for our top end wine named "The Velvet Bramble" I no exactly how i want the label to look and im searching for a talented designer to out my vision to life.

There will be 3 parts to this design.

Top Cover design with gold text wrapped around saying"The Velvet Bramble" (See Fig 2)

The front label which i want same as attached (See fig 2)

The Rear label
(See Fig 2 for design)
(See Fig 3 for content)

and final bottle design how it will look together

Come on guys keep the designs coming

Reason: I have extended my deadline due to the break from work over the Christmas new year period. Extra consideration will be made

Target Market(s)

The High End wine consumers the bottle cost will be $100USD

Font styles to use
Decorative
Script

Requirements
Must have

• Top Cover design with gold text wrapped around saying"The Velvet Bramble" (See Fig 2)
Black Rear Label with information and company name (Layout Fig 2) (Content Fig 3)
Gold and Black theme
The Text "Wine of Australia" somewhere on the bottle

```html
<!DOCTYPE html>
<html lang="en">
<head>
<meta charset="utf-8">
<title>The Velvet Bramble – Capsule and Front Label</title>
<link rel="stylesheet" href="https://fonts.googleapis.com/css2?family=Antonio:wght@600&family=Pinyon+Script&display=swap">
<style>
  :root {
    --page: #ffffff;
    --capsule-black: #141414;
    --capsule-sheen: #2a2a2a;
    --label-black: #1e1e1f;
    --gold: #d8b764;
    --gold-deep: #b8953f;
    --cream: #f4efe2;
  }
  html, body {
    margin: 0;
    padding: 0;
    width: 1200px;
    height: 1000px;
    overflow: hidden;
    background: var(--page);
  }
  .canvas {
    position: relative;
    width: 1200px;
    height: 1000px;
  }

  /* Top cover (capsule), shown flat */
  .top-cover {
    position: absolute;
    left: 524px;
    top: 30px;
    width: 152px;
    height: 150px;
  }
  .top-cover__lip {
    position: absolute;
    left: 0;
    top: 0;
    width: 152px;
    height: 30px;
    border-radius: 10px 10px 4px 4px;
    background: linear-gradient(90deg, var(--capsule-black), var(--capsule-sheen) 45%, var(--capsule-black));
  }
  .top-cover__sleeve {
    position: absolute;
    left: 8px;
    top: 30px;
    width: 136px;
    height: 120px;
    background: linear-gradient(90deg, var(--capsule-black), var(--capsule-sheen) 45%, var(--capsule-black));
  }

  /* Front label */
  .front-label {
    position: absolute;
    left: 414px;
    top: 212px;
    width: 372px;
    height: 745px;
    box-sizing: border-box;
    background: var(--label-black);
    border: 5px solid var(--gold);
  }
  .front-label__inner-frame {
    position: absolute;
    inset: 9px;
    border: 2px dotted var(--gold);
  }
  .wine-name {
    position: absolute;
    top: 170px;
    left: 0;
    right: 0;
    margin: 0;
    text-align: center;
    font-family: "Antonio", "Arial Narrow", sans-serif;
    font-weight: 600;
    font-size: 64px;
    line-height: 74px;
    letter-spacing: 1px;
    color: var(--gold);
    text-transform: uppercase;
  }
  .wine-name span { display: block; }
  .emblem-area {
    position: absolute;
    top: 420px;
    left: 50%;
    width: 58px;
    height: 78px;
    transform: translateX(-50%);
    background: radial-gradient(circle at 50% 40%, var(--gold) 0%, var(--gold-deep) 100%);
    border-radius: 6px;
    opacity: 0.85;
  }
  .origin {
    position: absolute;
    top: 574px;
    left: 0;
    right: 0;
    margin: 0;
    text-align: center;
    font-family: "Pinyon Script", cursive;
    font-size: 32px;
    color: var(--cream);
  }
</style>
</head>
<body>
  <main class="canvas">
    <div class="top-cover" aria-label="Black bottle capsule">
      <div class="top-cover__lip"></div>
      <div class="top-cover__sleeve"></div>
    </div>
    <section class="front-label" aria-label="Front wine label">
      <div class="front-label__inner-frame"></div>
      <h1 class="wine-name"><span>The</span><span>Velvet</span><span>Bramble</span></h1>
      <div class="emblem-area" role="img" aria-label="Gold grape cluster emblem"></div>
      <p class="origin">Wine of Australia</p>
    </section>
  </main>
</body>
</html>
```